Geschäftspapiere für Unternehmens- und Personalberatung
Zielgruppe
Unternehmens- und Personalberatung für Fach- und Führungskräfte, Zielgruppe meistens Akademiker*innen und Diplomingenieur*innen
Aufgabenstellung
nicht verschnörkelt, soll Menschen mit Jahresgehältern über 100.000 EUR ansprechen und seriös wirken

```html
<!DOCTYPE html>
<html lang="de">
<head>
<meta charset="utf-8">
<title>Velmoran Geschäftsausstattung</title>
<link href="https://fonts.googleapis.com/css2?family=Montserrat:wght@400;500;600&family=PT+Serif&display=swap" rel="stylesheet">
<style>
  :root {
    --teal: #026382;
    --slate: #7d9297;
    --pale: #e3e8ea;
    --pale-blue: #cfe0e6;
    --paper: #ffffff;
    --backdrop: #e8e8e8;
    --ink: #1a1a1a;
  }
  * { box-sizing: border-box; margin: 0; padding: 0; }
  html, body { width: 1200px; height: 833px; overflow: hidden; }
  body { background: var(--backdrop); position: relative; font-family: "Montserrat", sans-serif; }

  .wordmark {
    display: flex; align-items: center; gap: 6px;
    font-family: "Montserrat", sans-serif; font-weight: 600;
    color: var(--teal); letter-spacing: 0.3px; white-space: nowrap; position: absolute;
  }
  .wordmark .mark-square { background: var(--slate); display: block; }

  /* Letterhead */
  .letterhead { position: absolute; left: 51px; top: 78px; width: 520px; height: 720px; background: var(--paper); }
  .letterhead .wordmark { left: 33px; top: 28px; font-size: 24px; }
  .letterhead .mark-square { width: 32px; height: 32px; }
  .letterhead .header-rule { position: absolute; left: 0; top: 81px; width: 100%; height: 3px; background: var(--teal); }
  .letterhead .emblem-field { position: absolute; left: 150px; top: 262px; width: 219px; height: 211px; background: var(--pale); }
  .letterhead .emblem-field::before { content: ""; position: absolute; left: 0; top: 0; width: 58px; height: 121px; background: var(--pale-blue); clip-path: polygon(0 0, 100% 0, 0 100%); }
  .footer-info { position: absolute; left: 33px; top: 667px; display: flex; font-size: 5.6px; line-height: 1.45; color: var(--ink); }
  .footer-info .col { padding: 0 3px 0 3px; height: 42px; }
  .footer-info .col + .col { border-left: 1.2px solid var(--teal); }
  .letterhead .footer-band { position: absolute; left: 0; bottom: 0; width: 100%; height: 9px; background: var(--teal); }

  /* Business cards */
  .card { position: absolute; top: 154px; width: 226px; height: 129px; }
  .card-front { left: 637px; background: var(--teal); overflow: hidden; }
  .card-front .emblem-field { position: absolute; right: 0; top: 0; width: 80px; height: 78px; background: rgba(255,255,255,0.14); }
  .card-front .wordmark { left: 40px; top: 49px; font-size: 21px; color: var(--paper); }
  .card-front .mark-square { width: 26px; height: 26px; background: var(--paper); }
  .card-back { left: 887px; background: var(--paper); }
  .card-back .holder-name { position: absolute; left: 7px; top: 28px; font-family: "PT Serif", serif; font-size: 11.5px; color: var(--teal); }
  .card-back .wordmark { left: 128px; top: 26px; font-size: 12px; gap: 4px; }
  .card-back .mark-square { width: 14px; height: 14px; }
  .contact-rail { position: absolute; left: 0; top: 68px; width: 15px; height: 57px; background: var(--teal); border-radius: 0 7px 7px 0; }
  .contact-rail i { position: absolute; left: 3px; width: 8px; height: 8px; background: var(--paper); border-radius: 1px; }
  .contact-list { position: absolute; left: 19px; top: 67px; font-family: "PT Serif", serif; font-size: 8px; color: var(--teal); line-height: 11px; list-style: none; }
  .contact-list li.gap { margin-top: 5px; }

  /* Envelope */
  .envelope { position: absolute; left: 623px; top: 360px; width: 538px; height: 342px; }
  .envelope .flap { position: absolute; left: 0; top: 0; width: 538px; height: 76px; background: var(--teal); clip-path: polygon(1.9% 0, 98.7% 0, 100% 100%, 0 100%); border-radius: 12px 12px 0 0; }
  .envelope .body { position: absolute; left: 0; top: 76px; width: 538px; height: 266px; background: var(--paper); }
  .envelope .emblem-field { position: absolute; left: 0; top: 0; width: 101px; height: 98px; background: var(--pale); }
  .envelope .emblem-field::before { content: ""; position: absolute; left: 0; top: 0; width: 28px; height: 56px; background: var(--pale-blue); clip-path: polygon(0 0, 100% 0, 0 100%); }
  .envelope .address-window { position: absolute; left: 49px; top: 115px; width: 219px; height: 110px; background: var(--slate); border-radius: 4px; }
  .envelope .wordmark { left: 368px; top: 203px; font-size: 22px; }
  .envelope .mark-square { width: 30px; height: 30px; }
</style>
</head>
<body>

<section class="letterhead">
  <div class="wordmark"><span class="mark-square"></span>Velmoran</div>
  <div class="header-rule"></div>
  <div class="emblem-field" role="img" aria-label="Large faint brand emblem area"></div>
  <div class="footer-info">
    <div class="col">Name Company</div>
    <div class="col">Street Street Street<br>0000 City</div>
    <div class="col">Tel : 34(000)-000<br>Mobile: +00000000<br>Fax: 00000-000</div>
    <div class="col">info@namecompany.com<br>www.namecompany.com</div>
    <div class="col">FinanZamt<br>St--Nr-000/000/00<br>USt- ID DE00000</div>
    <div class="col">Brankverbindung<br>name of the brank<br>RLZ00000- Kto. 00000<br>IBAN DE0000000000<br>BIC/SWIFT-Code DE00000</div>
  </div>
  <div class="footer-band"></div>
</section>

<section class="card card-front">
  <div class="emblem-field" role="img" aria-label="Faint brand emblem area"></div>
  <div class="wordmark"><span class="mark-square"></span>Velmoran</div>
</section>

<section class="card card-back">
  <p class="holder-name">Jorin Talvecke</p>
  <div class="wordmark"><span class="mark-square"></span>Velmoran</div>
  <div class="contact-rail"><i style="top:6px"></i><i style="top:28px"></i><i style="top:45px"></i></div>
  <ul class="contact-list">
    <li>0031(0)6-40718235</li>
    <li>0031(0)88-7034412</li>
    <li class="gap">www.quellmarkt.nl</li>
    <li class="gap">jorin@quellmarkt.nl</li>
  </ul>
</section>

<section class="envelope">
  <div class="flap"></div>
  <div class="body">
    <div class="emblem-field" role="img" aria-label="Faint brand emblem area"></div>
    <div class="address-window"></div>
    <div class="wordmark"><span class="mark-square"></span>Velmoran</div>
  </div>
</section>

</body>
</html>
```